Veterinary Pylon

My veterinary clinic is not clearly visible from the street and I want to place a Pylon next to my driveway. I want a modern, elegant straight Design, the Photo shows the sheduled place. One can see the clinic on our Homepage: www.fernhollow-tierpraxis.at
The last pictures are examples for pylones I like

Target Market(s)

the passing cars often miss my entry...I want to show where to turn left

Colors
3276b5
33a6d7
00a990

Requirements
Must have
• High value, simple elegance, size: 250cm (high) x 100cm (width)
Nice to have
• Our Logo, arrow(?)

A special Text is not necessary but this will be an option:

Biegen sie hier ab und wir biegen es wieder hin!
Should not have
• Too much Color, the colors I have chosen are the possible colors but it‘s not necessary to use them.

```html
<!DOCTYPE html>
<html lang="de">
<head>
<meta charset="utf-8">
<title>Fernhollow Tierpraxis – Pylon</title>
<link rel="stylesheet" href="https://fonts.googleapis.com/css2?family=Montserrat:wght@600;700&display=swap">
<style>
  :root {
    --navy: #2b4a8e;
    --sky: #3cb8dd;
    --sky-pale: #d8eefa;
    --paper: #ffffff;
    --stage: #eef1f4;
  }
  * { box-sizing: border-box; margin: 0; padding: 0; }
  html, body {
    width: 818px;
    height: 1200px;
    overflow: hidden;
    background: var(--stage);
    font-family: "Montserrat", sans-serif;
  }
  .pylon {
    position: absolute;
    left: 176px;
    top: 20px;
    width: 466px;
    height: 1160px;
    background: linear-gradient(180deg, var(--paper) 0%, var(--paper) 45%, #eaf5fc 62%, var(--sky-pale) 100%);
    overflow: hidden;
    box-shadow: 0 6px 24px rgba(20, 40, 80, 0.18);
  }
  .brand {
    position: absolute;
    left: 0;
    top: 120px;
    width: 100%;
    text-align: center;
  }
  .brand-dot {
    display: block;
    width: 96px;
    height: 96px;
    margin: 0 auto 34px;
    border-radius: 50%;
    background: var(--sky);
  }
  .brand-name {
    color: var(--navy);
    font-weight: 700;
    font-size: 52px;
    line-height: 1.05;
    letter-spacing: 0.5px;
  }
  .turn-arrow {
    position: absolute;
    left: 97px;
    top: 465px;
    width: 272px;
    height: 124px;
  }
  .headline {
    position: absolute;
    left: 55px;
    top: 598px;
    width: 400px;
    color: var(--navy);
    font-weight: 700;
    font-size: 40px;
    line-height: 50px;
  }
  .photo-stethoscope {
    position: absolute;
    left: 0;
    top: 752px;
    width: 100%;
    height: 408px;
    background:
      radial-gradient(ellipse 55% 45% at 60% 35%, #2f7fd0 0%, #5aa8e6 45%, rgba(140, 200, 240, 0) 75%),
      linear-gradient(180deg, #e6f4fc 0%, #9fd3f1 45%, #5fb4e8 100%);
  }
  .web-bar {
    position: absolute;
    left: 55px;
    top: 1058px;
    width: 411px;
    height: 53px;
    background: var(--navy);
    color: var(--paper);
    font-weight: 600;
    font-size: 19px;
    display: flex;
    align-items: center;
    justify-content: center;
    letter-spacing: 0.2px;
  }
</style>
</head>
<body>
  <main class="pylon">
    <div class="brand">
      <span class="brand-dot"></span>
      <p class="brand-name">Fernhollow<br>Tierpraxis</p>
    </div>

    <svg class="turn-arrow" viewBox="0 0 272 124" aria-label="Links abbiegen">
      <path d="M66 16 L16 62 L66 108 M18 62 L256 62"
            fill="none" stroke="var(--navy)" stroke-width="30"
            stroke-linecap="round" stroke-linejoin="round"/>
    </svg>

    <h1 class="headline">Biegen Sie ein,<br>dann biegen wir<br>es hin!</h1>

    <div class="photo-stethoscope" role="img" aria-label="Foto eines blauen Stethoskops auf spiegelnder Fläche"></div>

    <div class="web-bar">www.fernhollow-tierpraxis.at</div>
  </main>
</body>
</html>
```